Business Card for Voltrix

Horizontal business card for voltrix, the electrical contractor.
clean and professional looking, using company branding and colours.
I also want the blue in the logo and wording to be made a more 'electric' blue and the grey 'Voltrix' to be slightly darker.

Pleas use the following contact details:

Peter Alwick
Owner

t: 01632 960581
m: 07700 900316
e: peter@voltrix-wiring.co.uk

www.voltrix-wiring.co.uk

Industry/Entity Type

Electrical

Font styles to use
Sans Serif

```html
<!DOCTYPE html>
<html lang="en">
<head>
<meta charset="utf-8">
<title>Voltrix business card</title>
<link href="https://fonts.googleapis.com/css2?family=Quicksand:wght@400;500;600&display=swap" rel="stylesheet">
<style>
  :root {
    --page-bg: #f3f1ea;
    --card-bg: #ffffff;
    --brand-grey: #4a4f4b;
    --electric-blue: #00a9d8;
    --wash-dark: #c3c8bd;
    --wash-mid: #dfe3da;
    --wash-light: #ffffff;
    --text-dark: #2f3331;
    --divider: #b9bdb6;
  }
  * { margin: 0; padding: 0; box-sizing: border-box; }
  html, body {
    width: 1200px; height: 843px; overflow: hidden;
    background: var(--page-bg);
    font-family: "Quicksand", sans-serif;
  }
  .card-sheet { position: relative; width: 1200px; height: 843px; }
  .card {
    position: absolute; top: 272px;
    width: 525px; height: 300px;
    background: var(--card-bg);
    border-radius: 8px;
    overflow: hidden;
    box-shadow: 0 6px 18px rgba(0,0,0,0.18);
  }
  .card--front { left: 50px; }
  .card--back { left: 625px; }
  .card__wash {
    position: absolute; left: 0; right: 0; bottom: 0;
    background: linear-gradient(to bottom, var(--wash-light) 0%, var(--wash-mid) 45%, var(--wash-dark) 100%);
  }
  .card--front .card__wash { top: 140px; }
  .card--back .card__wash { top: 185px; }
  .brand { position: absolute; }
  .brand__name {
    display: flex; align-items: center; gap: 10px;
    color: var(--brand-grey);
    font-weight: 600; text-transform: uppercase;
    letter-spacing: 0.18em; line-height: 1;
  }
  .brand__dot {
    width: 0.7em; height: 0.7em; border-radius: 50%;
    background: var(--electric-blue);
  }
  .brand__tagline {
    color: var(--electric-blue);
    font-weight: 500; text-transform: uppercase;
    letter-spacing: 0.08em; margin-top: 4px;
  }
  .card--front .brand { left: 100px; top: 52px; }
  .card--front .brand__name { font-size: 46px; }
  .card--front .brand__tagline { font-size: 15px; padding-left: 40px; }
  .card--back .brand { left: 30px; top: 48px; }
  .card--back .brand__name { font-size: 30px; gap: 8px; }
  .card--back .brand__tagline { font-size: 10px; padding-left: 28px; }
  .card__divider {
    position: absolute; left: 300px; top: 40px;
    width: 1px; height: 125px; background: var(--divider);
  }
  .contact { position: absolute; left: 314px; top: 58px; color: var(--text-dark); }
  .contact__name { font-size: 22px; color: var(--electric-blue); font-weight: 400; line-height: 1.1; }
  .contact__role { font-size: 13px; margin-bottom: 14px; }
  .contact__line { font-size: 11.5px; line-height: 1.55; }
</style>
</head>
<body>
<main class="card-sheet">

  <section class="card card--front" aria-label="Card front">
    <div class="card__wash" role="img" aria-label="Decorative grey and blue wave graphic across the lower card"></div>
    <div class="brand">
      <div class="brand__name"><span class="brand__dot"></span>Voltrix</div>
      <div class="brand__tagline">The Electrical Contractor</div>
    </div>
  </section>

  <section class="card card--back" aria-label="Card back">
    <div class="card__wash" role="img" aria-label="Decorative grey and blue wave graphic across the lower card"></div>
    <div class="brand">
      <div class="brand__name"><span class="brand__dot"></span>Voltrix</div>
      <div class="brand__tagline">The Electrical Contractor</div>
    </div>
    <div class="card__divider"></div>
    <div class="contact">
      <p class="contact__name">Peter Alwick</p>
      <p class="contact__role">Owner</p>
      <p class="contact__line">01632 960581 / 07700 900316</p>
      <p class="contact__line">peter@voltrix-wiring.co.uk</p>
      <p class="contact__line">www.voltrix-wiring.co.uk</p>
    </div>
  </section>

</main>
</body>
</html>
```